Skyward Aviatrix pilot

I am looking for a personal business card, for a very well qualified female pilot, with a lot of aviation experience.

Currently an airline pilot, have worked as a bush pilot in Africa, looking to get into corporate aviation, or private jet owners.
Want a classy looking card for networking...

Could be interested in a retro\vintage look also?!

An idea,, is an african sunset background, with my wings\logo on it
Updates

I just want to say thank you to all of your for your amazing designs!

I have been very busy flying this past week , so not had a chance to be on the computer much.
But I provide some feedback, and conclusions very soon!
Thank you again.

Marla

Reason: Still waiting on a couple of revisions to be 100% about my choice!

Target Market(s)

corporate aviation, private jet owners, casino's,
General audience.
networking

Industry/Entity Type

Airline

Requirements
Nice to have
• Classy, edgy, sexy, but also feminine

```html
<!DOCTYPE html>
<html lang="en">
<head>
<meta charset="utf-8">
<title>Skyward Aviatrix – Business Card</title>
<link rel="stylesheet" href="https://fonts.googleapis.com/css2?family=Open+Sans:wght@400;700&display=swap">
<style>
  :root {
    --stage: #e9e6e1;
    --card-black-top: #3a3d40;
    --card-black-bottom: #0e0f10;
    --card-white: #f7f7f6;
    --card-white-edge: #e2e2e0;
    --gold: #c9a24a;
    --gold-light: #ead08a;
    --gold-dark: #8a6a22;
    --ink: #111111;
    --ring-fill: #1c1e20;
  }
  * { box-sizing: border-box; margin: 0; padding: 0; }
  html, body {
    width: 1200px;
    height: 900px;
    overflow: hidden;
  }
  body {
    background: var(--stage);
    font-family: "Open Sans", Arial, sans-serif;
    display: flex;
    align-items: center;
    justify-content: center;
    gap: 70px;
  }
  .card {
    width: 340px;
    height: 600px;
    position: relative;
    box-shadow: 0 10px 30px rgba(0,0,0,0.25);
  }

  /* Front */
  .card-front {
    background: linear-gradient(180deg, var(--card-black-top) 0%, #1e2022 55%, var(--card-black-bottom) 100%);
  }
  .front-emblem {
    position: absolute;
    top: 90px;
    left: 50%;
    transform: translateX(-50%);
    display: flex;
    flex-direction: column;
    align-items: center;
    gap: 22px;
  }
  .emblem-ring {
    width: 230px;
    height: 230px;
    border-radius: 50%;
    border: 7px solid var(--gold);
    background: var(--ring-fill);
  }
  .brand-name {
    font-family: "Open Sans", Arial, sans-serif;
    font-weight: 700;
    color: var(--gold);
    white-space: nowrap;
  }
  .front-emblem .brand-name {
    font-size: 30px;
    letter-spacing: 0.5px;
  }
  .gold-stripes {
    position: absolute;
    left: 0;
    right: 0;
    bottom: 40px;
  }

  /* Back */
  .card-back {
    background: linear-gradient(160deg, #ffffff 0%, var(--card-white) 50%, var(--card-white-edge) 100%);
    text-align: center;
    color: var(--ink);
  }
  .back-emblem {
    position: absolute;
    top: 70px;
    left: 0;
    right: 0;
    display: flex;
    flex-direction: column;
    align-items: center;
    gap: 12px;
  }
  .back-emblem .emblem-ring {
    width: 120px;
    height: 120px;
    border-width: 4px;
  }
  .back-emblem .brand-name {
    font-size: 17px;
  }
  .contact {
    position: absolute;
    top: 300px;
    left: 0;
    right: 0;
  }
  .contact-name {
    font-size: 21px;
    font-weight: 700;
    margin-bottom: 32px;
  }
  .contact-line {
    font-size: 15.5px;
    line-height: 1.4;
  }
  .contact-address {
    margin-top: 22px;
  }
</style>
</head>
<body>

  <section class="card card-front" aria-label="Card front">
    <div class="front-emblem">
      <div class="emblem-ring"></div>
      <span class="brand-name">Skyward Aviatrix</span>
    </div>
    <svg class="gold-stripes" width="340" height="110" viewBox="0 0 340 110" aria-hidden="true">
      <defs>
        <linearGradient id="stripe-gold" x1="0" y1="0" x2="1" y2="0">
          <stop offset="0" stop-color="#8a6a22"/>
          <stop offset="0.35" stop-color="#ead08a"/>
          <stop offset="0.65" stop-color="#c9a24a"/>
          <stop offset="1" stop-color="#8a6a22"/>
        </linearGradient>
      </defs>
      <rect x="0" y="8" width="340" height="20" fill="url(#stripe-gold)"/>
      <rect x="0" y="42" width="340" height="20" fill="url(#stripe-gold)"/>
      <rect x="0" y="76" width="340" height="20" fill="url(#stripe-gold)"/>
    </svg>
  </section>

  <section class="card card-back" aria-label="Card back">
    <div class="back-emblem">
      <div class="emblem-ring"></div>
      <span class="brand-name">Skyward Aviatrix</span>
    </div>
    <div class="contact">
      <p class="contact-name">Capt. Fiona Marla</p>
      <p class="contact-line">1-555-204-7310</p>
      <p class="contact-line">fionamarlacaptain@mail.com</p>
      <div class="contact-address">
        <p class="contact-line">1800 Harbor View Road</p>
        <p class="contact-line">Seaview, CA 90000</p>
      </div>
    </div>
  </section>

</body>
</html>
```